The Ashcombe- outdoor banner

This should be a horizontal banner. It should have the logos attached incorporated and the following details
Coming Spring 2025: The Ashcombe - Exclusive Luxury Condos
Listed by Marisol Avenell | Quillfield Realty
Construction by Pinegate Builders
Unveil the height of luxury living with The Ashcombe, a new condo building in East Boston, set for completion in Spring 2025. Experience a standard of elegance and sophistication like never before.
For more information and inquiries, please contact:
Marisol Avenell
Phone: (617) 490-7163
Email: marisol@quillfieldhomes.example
The banner should be very classy incorporting gold and navy very classic fonts. The Ashcombe should look very classy and exclusive. The pinegate builders logo should be smaller. It should not include their phone number and instagram handle only the name of the company. Herringbone pattern in the background would be great. This is going outside the building to advertise pre construction units

```html
<!DOCTYPE html>
<html lang="en">
<head>
<meta charset="UTF-8">
<title>The Ashcombe – Exclusive Luxury Condos</title>
<link rel="stylesheet" href="https://fonts.googleapis.com/css2?family=Oswald:wght@600&family=Playfair+Display:ital,wght@0,400;1,400&family=Poppins:wght@300;400;500&display=swap">
<style>
  :root {
    --navy: #263552;
    --gold: #eab86d;
    --gold-soft: #e3b872;
    --ink: #1f2c45;
    --rule: #7d879b;
    --label: #c7cbd4;
    --light: #eceae4;
  }
  html, body {
    margin: 0;
    padding: 0;
    overflow: hidden;
    background: var(--navy);
  }
  .banner {
    position: relative;
    width: 1200px;
    height: 599px;
    background: var(--navy);
    overflow: hidden;
    font-family: "Poppins", sans-serif;
    color: var(--gold);
  }
  .ribbon {
    position: absolute;
    left: 0;
    top: 32px;
    width: 390px;
    height: 37px;
  }
  .ribbon svg { position: absolute; inset: 0; }
  .ribbon-text {
    position: absolute;
    left: 75px;
    top: 0;
    line-height: 37px;
    font-family: "Oswald", sans-serif;
    font-weight: 600;
    font-size: 23px;
    letter-spacing: 0.09em;
    color: var(--ink);
  }
  .title {
    position: absolute;
    left: 76px;
    top: 88px;
    margin: 0;
    font-family: "Playfair Display", serif;
    font-weight: 400;
    color: var(--gold);
  }
  .title-article {
    display: block;
    margin-left: 70px;
    font-style: italic;
    font-size: 62px;
    line-height: 60px;
  }
  .title-name {
    display: block;
    font-size: 108px;
    line-height: 104px;
    letter-spacing: -0.01em;
  }
  .tagline {
    position: absolute;
    right: 48px;
    top: 100px;
    text-align: right;
    font-weight: 500;
    font-size: 15px;
    letter-spacing: 0.58em;
    line-height: 32px;
    text-transform: uppercase;
  }
  .intro {
    position: absolute;
    left: 77px;
    top: 272px;
    width: 1060px;
    margin: 0;
    font-weight: 400;
    font-size: 21.5px;
    line-height: 39px;
    color: var(--gold-soft);
  }
  .divider {
    position: absolute;
    left: 71px;
    top: 419px;
    width: 1059px;
    height: 1px;
    background: var(--rule);
  }
  .credits {
    position: absolute;
    left: 0;
    top: 459px;
    width: 1200px;
    height: 110px;
  }
  .credit {
    position: absolute;
    top: 0;
    height: 110px;
    text-align: center;
  }
  .credit-listing { left: 60px; width: 372px; }
  .credit-build { left: 433px; width: 398px; }
  .credit-contact { left: 831px; width: 360px; }
  .credit-listing, .credit-build { border-right: 1px solid var(--rule); }
  .credit-listing { border-right: 1px solid var(--rule); }
  .credit-build { border-left: 0; }
  .label {
    margin: 0;
    font-size: 10px;
    letter-spacing: 0.06em;
    line-height: 13px;
    text-transform: uppercase;
    color: var(--label);
  }
  .listing-brand {
    display: flex;
    align-items: center;
    justify-content: center;
    gap: 14px;
    margin-top: 22px;
  }
  .brand-dot {
    width: 50px;
    height: 50px;
    border: 2px solid var(--gold);
    border-radius: 50%;
    box-sizing: border-box;
  }
  .brand-name {
    font-family: "Playfair Display", serif;
    font-weight: 400;
    font-size: 24px;
    letter-spacing: 0.04em;
    text-transform: uppercase;
    color: var(--gold);
  }
  .builder-name {
    margin-top: 36px;
    font-family: "Oswald", sans-serif;
    font-weight: 600;
    font-size: 20px;
    letter-spacing: 0.06em;
    text-transform: uppercase;
    color: var(--gold);
  }
  .contact-name {
    margin: 8px 0 2px;
    font-family: "Playfair Display", serif;
    font-weight: 400;
    font-size: 29px;
    line-height: 34px;
    color: var(--gold);
  }
  .contact-line {
    margin: 0;
    font-size: 14.5px;
    line-height: 19px;
    color: var(--light);
  }
  .contact-line svg {
    width: 12px;
    height: 12px;
    vertical-align: -1px;
    margin-right: 4px;
  }
</style>
</head>
<body>
<main class="banner">
  <div class="ribbon">
    <svg width="390" height="37" viewBox="0 0 390 37" aria-hidden="true">
      <polygon points="0,0 390,0 370,18.5 390,37 0,37" fill="var(--gold)"/>
    </svg>
    <span class="ribbon-text">COMING SPRING 2025</span>
  </div>

  <h1 class="title">
    <span class="title-article">The</span>
    <span class="title-name">Ashcombe</span>
  </h1>

  <p class="tagline">Exclusive<br>Luxury Condos</p>

  <p class="intro">Unveil the height of luxury living with The Ashcombe, a new condo building in East Boston, set for completion in Spring 2025. Experience a standard of elegance and sophistication like never before.</p>

  <div class="divider"></div>

  <section class="credits">
    <div class="credit credit-listing">
      <p class="label">Listed by:</p>
      <div class="listing-brand">
        <span class="brand-dot"></span>
        <span class="brand-name">Quillfield Realty</span>
      </div>
    </div>

    <div class="credit credit-build">
      <p class="label">Construction by:</p>
      <div class="builder-name">Pinegate Builders</div>
    </div>

    <div class="credit credit-contact">
      <p class="label">For more information and inquiries,<br>please contact:</p>
      <p class="contact-name">Marisol Avenell</p>
      <p class="contact-line">marisol@quillfieldhomes.example</p>
      <p class="contact-line">
        <svg viewBox="0 0 24 24" aria-hidden="true"><path fill="var(--light)" d="M6.6 10.8a15.1 15.1 0 0 0 6.6 6.6l2.2-2.2a1 1 0 0 1 1-.25 11.4 11.4 0 0 0 3.6.57 1 1 0 0 1 1 1V20a1 1 0 0 1-1 1A17 17 0 0 1 3 4a1 1 0 0 1 1-1h3.5a1 1 0 0 1 1 1c0 1.25.2 2.45.57 3.57a1 1 0 0 1-.25 1z"/></svg>(617) 490-7163
      </p>
    </div>
  </section>
</main>
</body>
</html>
```